Wild Mo's Wine Label Project

We need a new entry level wine label called "Wild Mo's" for a range of wines we are developing from inland Australia. Our company is made up of three youngish guys who live hard and love taking the mickey. Wild Mo is Wild Moss - the largest and loudest of the three partners (and ideally this label will take the mickey out of him). We've grown the grapes ourselves for this first release which will be a 2012 Pinot Gris. Wine style is dry, young, fresh and contemporary and pitched at the sub AUD $10 retail price point. The package will be flint (clear) claret shape bottle with plain screwcap (colour matched to suit the winning label design).

I've attached a couple of photos of Wild Moss to give you some idea of his presence and persona.

Target Market(s)

Semi educated 25 - 40 year old wine drinkers. Skewed towards females.

Industry/Entity Type

Retail

Requirements
Should not have
• Anything traditional or old fashioned

```html
<!DOCTYPE html>
<html lang="en">
<head>
<meta charset="utf-8">
<title>Wild Mo's 2012 Pinot Gris Label</title>
<link rel="stylesheet" href="https://fonts.googleapis.com/css2?family=Arimo:wght@400;700&display=swap">
<style>
  :root {
    --paper: #ffffff;
    --ink: #1a1a1a;
    --seal: #111111;
    --seal-text: #ffffff;
    --varietal-pink: #e8418c;
    --cap-pink: #f0307e;
    --wine-light: #f3efc4;
    --wine-mid: #d9d09a;
    --wine-dark: #bfb477;
    --label-shadow: rgba(0, 0, 0, 0.25);
  }
  html, body {
    margin: 0;
    padding: 0;
    overflow: hidden;
  }
  body {
    width: 1200px;
    height: 1031px;
    background: var(--paper);
    position: relative;
    font-family: "Arimo", Arial, sans-serif;
  }
  .wine-label {
    position: absolute;
    left: 158px;
    top: 354px;
    width: 388px;
    height: 374px;
    background: var(--paper);
    box-shadow: 2px 5px 14px var(--label-shadow);
  }
  .brand-seal {
    position: absolute;
    left: 156px;
    top: 131px;
    width: 398px;
    height: 398px;
    border-radius: 50%;
    background: var(--seal);
    display: flex;
    align-items: center;
    justify-content: center;
  }
  .brand-seal__name {
    color: var(--seal-text);
    font-weight: 700;
    font-size: 92px;
    line-height: 0.95;
    letter-spacing: 2px;
    text-transform: uppercase;
    text-align: center;
    margin: 0;
  }
  .label-details {
    position: absolute;
    left: 158px;
    top: 574px;
    width: 388px;
    text-align: center;
  }
  .label-details__vintage,
  .label-details__varietal {
    font-size: 50px;
    font-weight: 400;
    margin: 0;
    line-height: 1.12;
  }
  .label-details__vintage { color: var(--ink); }
  .label-details__varietal { color: var(--varietal-pink); }
  .brand-wordmark {
    position: absolute;
    left: 40px;
    top: 848px;
    color: var(--ink);
    font-weight: 700;
    font-size: 66px;
    line-height: 0.95;
    text-transform: uppercase;
    margin: 0;
  }
  .bottle-shot {
    position: absolute;
    left: 780px;
    top: 94px;
    width: 178px;
    height: 884px;
  }
</style>
</head>
<body>
  <div class="wine-label"></div>
  <div class="brand-seal">
    <p class="brand-seal__name">Wild<br>Mo's</p>
  </div>
  <div class="label-details">
    <p class="label-details__vintage">2012</p>
    <p class="label-details__varietal">Pinot Gris</p>
  </div>
  <p class="brand-wordmark">Wild<br>Mo's</p>

  <svg class="bottle-shot" role="img" aria-label="Clear claret bottle of Pinot Gris with pink screwcap and the Wild Mo's label" viewBox="0 0 178 884">
    <defs>
      <linearGradient id="wine-body" x1="0" y1="0" x2="1" y2="0">
        <stop offset="0" stop-color="var(--wine-dark)"/>
        <stop offset="0.45" stop-color="var(--wine-light)"/>
        <stop offset="1" stop-color="var(--wine-mid)"/>
      </linearGradient>
    </defs>
    <rect x="56" y="0" width="66" height="120" rx="6" fill="var(--cap-pink)"/>
    <path d="M58 120 H120 V240 C120 300 176 320 176 380 V864 Q176 884 156 884 H22 Q2 884 2 864 V380 C2 320 58 300 58 240 Z" fill="url(#wine-body)"/>
  </svg>
</body>
</html>
```